New business card for civil engineering company - "Keystone Audit"

We need a business card designed for our new structural engineering company.

The company name is "Keystone Audit" logo files attached.

We would like the following:
* Two-sided card
* Simple design

Information to be placed on the card:
Name - Marcus Dellow
Job Title - Director / Structural Engineer
Credentials - BEng(Hons), CPEng, CMengNZ, IntPE(NZ)
Email - marcus.dellow@keystoneaudit.co.nz
mobile - 0219364058
website - www.keystoneaudit.co.nz

```html
<!DOCTYPE html>
<html lang="en">
<head>
<meta charset="utf-8">
<title>Keystone Audit — Business Card</title>
<link rel="stylesheet" href="https://fonts.googleapis.com/css2?family=Montserrat:wght@400;500;700&display=swap">
<style>
  :root {
    --bg: #e6e6e6;
    --card-white: #ffffff;
    --navy: #124574;
    --brand-blue: #2f7cc4;
    --text-grey: #6f7780;
    --pale-blue: #a9d0f0;
    --sky-blue: #8cc0ea;
    --mid-blue: #5b93cf;
    --deep-blue: #3f78b5;
  }
  * { box-sizing: border-box; margin: 0; padding: 0; }
  html, body {
    width: 1200px; height: 900px; overflow: hidden;
    background: var(--bg);
    font-family: "Montserrat", sans-serif;
  }
  .canvas {
    width: 1200px; height: 900px;
    display: flex; align-items: center; justify-content: center; gap: 60px;
  }
  .card {
    position: relative;
    width: 520px; height: 318px;
    overflow: hidden;
    box-shadow: 0 10px 28px rgba(0,0,0,0.12);
  }
  .card-front { background: var(--card-white); }
  .card-front .accent-shapes {
    position: absolute; inset: 0; width: 100%; height: 100%;
  }
  .identity { position: absolute; left: 34px; top: 112px; }
  .person-name {
    font-weight: 700; font-size: 27px; letter-spacing: 0.5px;
    color: var(--brand-blue); text-transform: uppercase;
  }
  .person-role {
    margin-top: 6px; font-size: 9.5px; color: var(--text-grey);
    font-weight: 500;
  }
  .person-role .divider { margin: 0 6px; color: var(--brand-blue); }
  .contact-list {
    position: absolute; left: 34px; bottom: 30px;
    list-style: none; display: flex; flex-direction: column; gap: 6px;
  }
  .contact-item {
    display: flex; align-items: center; gap: 9px;
    font-size: 9.5px; color: var(--text-grey); font-weight: 500;
  }
  .contact-icon { width: 11px; height: 11px; flex: none; }
  .card-back {
    background: var(--navy);
    display: flex; align-items: center; justify-content: center;
  }
  .brand-lockup { text-align: center; color: #ffffff; }
  .brand-name {
    font-weight: 700; font-size: 26px; letter-spacing: 2px;
    text-transform: uppercase;
  }
  .brand-tagline {
    margin-top: 6px; font-size: 8.5px; letter-spacing: 3px;
    text-transform: uppercase; font-weight: 500; opacity: 0.85;
  }
</style>
</head>
<body>
<main class="canvas">
  <section class="card card-front" aria-label="Business card front">
    <svg class="accent-shapes" viewBox="0 0 520 318" aria-hidden="true">
      <polygon points="410,0 520,0 520,160" fill="var(--pale-blue)"/>
      <polygon points="468,0 520,0 520,112" fill="var(--sky-blue)"/>
      <polygon points="215,318 520,318 520,112" fill="var(--deep-blue)"/>
      <polygon points="430,175 520,112 520,200" fill="var(--mid-blue)"/>
    </svg>
    <div class="identity">
      <h1 class="person-name">Marcus Dellow</h1>
      <p class="person-role">Director / Structural Engineer<span class="divider">|</span>BEng(Hons), CPEng, CMengNZ, IntPE(NZ)</p>
    </div>
    <ul class="contact-list">
      <li class="contact-item">
        <svg class="contact-icon" viewBox="0 0 12 12" aria-hidden="true"><path d="M3 1 L5 3.2 L3.9 4.6 Q5 7 7.4 8.1 L8.8 7 L11 9 L9.6 11 Q4.5 10.5 1 2.4 Z" fill="var(--brand-blue)"/></svg>
        0219 364 058
      </li>
      <li class="contact-item">
        <svg class="contact-icon" viewBox="0 0 12 12" aria-hidden="true"><rect x="1" y="2.5" width="10" height="7" rx="1" fill="none" stroke="var(--brand-blue)" stroke-width="1.2"/><path d="M1.5 3 L6 6.5 L10.5 3" fill="none" stroke="var(--brand-blue)" stroke-width="1.2"/></svg>
        marcus.dellow@keystoneaudit.co.nz
      </li>
      <li class="contact-item">
        <svg class="contact-icon" viewBox="0 0 12 12" aria-hidden="true"><circle cx="6" cy="6" r="5" fill="none" stroke="var(--brand-blue)" stroke-width="1.1"/><ellipse cx="6" cy="6" rx="2.2" ry="5" fill="none" stroke="var(--brand-blue)" stroke-width="1"/><path d="M1 6 H11" stroke="var(--brand-blue)" stroke-width="1"/></svg>
        www.keystoneaudit.co.nz
      </li>
    </ul>
  </section>

  <section class="card card-back" aria-label="Business card back">
    <div class="brand-lockup">
      <p class="brand-name">Keystone Audit</p>
      <p class="brand-tagline">Peer Review Specialists</p>
    </div>
  </section>
</main>
</body>
</html>
```